Tailbrook Website Design

Need a website for a Dog Grooiming business. Please make it simular to these:

https://www.furvanto.com
https://haulnorix.com
https://meadowpetrin.com
https://www.drivelumo.com/search/

```html
<!DOCTYPE html>
<html lang="en">
<head>
<meta charset="utf-8">
<title>Tailbrook Dog Grooming</title>
<link href="https://fonts.googleapis.com/css2?family=Ubuntu:wght@400;500;700&family=Open+Sans:wght@400;600&display=swap" rel="stylesheet">
<style>
:root{
  --brown:#3b1d0e;
  --lime:#aec81c;
  --lime-dark:#9bb515;
  --ink:#222;
  --muted:#555;
  --white:#fff;
  --line:#ddd;
}
*{box-sizing:border-box;margin:0;padding:0}
html,body{width:1200px;height:3540px;overflow:hidden}
body{font-family:"Open Sans",sans-serif;color:var(--ink);background:var(--white);position:relative}
h1,h2,h3,h4,.logo{font-family:"Ubuntu",sans-serif}
.abs{position:absolute}

/* header */
.topbar{position:absolute;left:0;top:0;width:1200px;height:48px;background:var(--brown)}
.contact-item{position:absolute;top:6px;color:var(--white);font-size:12px;line-height:17px;padding-left:26px}
.contact-item b{display:block;font-size:13px}
.contact-item svg{position:absolute;left:0;top:8px}
.logo-tab{position:absolute;left:96px;top:0;width:200px;height:100px;background:var(--white);border-radius:0 0 50px 50px;display:flex;align-items:center;justify-content:center;gap:10px}
.logo-dot{width:26px;height:26px;border-radius:50%;background:var(--lime)}
.logo{font-size:26px;font-weight:700;color:var(--brown)}
.nav{position:absolute;top:48px;left:0;width:1200px;height:72px}
.nav ul{position:absolute;left:432px;top:26px;display:flex;gap:34px;list-style:none;font-size:15px}
.social{position:absolute;top:22px;display:flex;gap:12px}
.social span{width:28px;height:28px;border-radius:50%;background:var(--lime);display:block}

/* hero */
.hero{position:absolute;left:0;top:120px;width:1200px;height:570px;background:linear-gradient(90deg,#5a3a2a 0%,#8b6a55 35%,#b89478 60%,#7a5a44 100%)}
.hero h1{position:absolute;left:100px;top:180px;color:var(--white);font-size:44px;line-height:52px;font-weight:700}
.hero p{position:absolute;left:100px;top:296px;width:340px;color:var(--white);font-size:14px;line-height:22px}
.btn{display:inline-flex;align-items:center;gap:8px;border-radius:30px;font-size:13px;font-weight:600;padding:0 22px;height:36px}
.btn i{width:16px;height:16px;border-radius:50%;display:inline-block}
.btn-lime{background:var(--lime);color:var(--white)}
.btn-lime i{background:var(--white)}
.btn-brown{background:var(--brown);color:var(--white)}
.btn-brown i{background:var(--white)}
.btn-white{background:var(--white);color:var(--brown)}
.btn-white i{background:var(--lime)}

/* section titles */
.sec-title{position:absolute;left:0;width:1200px;text-align:center;font-size:32px;font-weight:700}
.sec-lead{position:absolute;left:350px;width:500px;text-align:center;font-size:14px;line-height:24px;color:var(--muted)}

/* grooming cards */
.card{position:absolute;top:930px;width:300px;height:400px;text-align:center}
.card.featured{background:var(--white);box-shadow:0 6px 26px rgba(0,0,0,.14);border-radius:14px}
.card-img{position:absolute;left:60px;top:30px;width:180px;height:150px;border-radius:10px}
.card h3{position:absolute;left:0;top:206px;width:300px;font-size:24px}
.card p{position:absolute;left:40px;top:248px;width:220px;font-size:13px;line-height:21px;color:var(--muted)}
.card .btn{position:absolute;left:88px;top:336px}

/* services */
.services{position:absolute;left:0;top:1440px;width:1200px;height:700px;background:var(--lime)}
.services .sec-title{top:60px;color:var(--white)}
.services .sec-lead{top:112px;color:var(--white)}
.svc{position:absolute;width:300px;color:var(--white)}
.svc .num{position:absolute;left:0;top:4px;font-family:"Ubuntu",sans-serif;font-size:70px;font-weight:400;line-height:70px}
.svc h4{position:absolute;left:54px;top:0;font-size:24px}
.svc p{position:absolute;left:54px;top:36px;width:240px;font-size:13px;line-height:20px}
.svc .btn{position:absolute;left:54px;top:104px}
.svc-photo{position:absolute;left:470px;top:160px;width:260px;height:500px;border-radius:130px 130px 10px 10px;background:radial-gradient(ellipse at 50% 45%,#e8c08a 0%,#d19c5e 45%,#a7c21c 80%)}

/* work */
.work-img{position:absolute;top:2370px;width:320px;height:376px}
.work-label{position:absolute;left:0;top:168px;width:320px;text-align:center;color:var(--white);font-family:"Ubuntu",sans-serif;font-size:30px;font-weight:500}

/* newsletter */
.newsletter{position:absolute;left:0;top:2824px;width:1200px;height:216px;background:var(--lime)}
.newsletter h2{position:absolute;left:100px;top:76px;color:var(--white);font-size:34px}
.newsletter p{position:absolute;left:100px;top:124px;color:var(--white);font-size:13px}
.field{position:absolute;left:600px;top:84px;width:360px;height:48px;border-radius:30px;background:var(--white);font-size:14px;color:#888;padding:14px 22px}
.submit{position:absolute;left:976px;top:84px;width:110px;height:48px;border-radius:30px;border:2px solid var(--white);color:var(--white);font-size:15px;font-weight:600;text-align:center;line-height:44px}

/* footer */
.foot-col{position:absolute;top:3100px}
.foot-col h4{font-size:22px;margin-bottom:20px}
.foot-logo{display:flex;align-items:center;gap:10px;margin-bottom:22px}
.foot-info{font-size:13px;line-height:28px}
.foot-info b{font-weight:600}
.foot-social{display:flex;gap:12px;margin-top:16px}
.foot-social span{width:34px;height:34px;border-radius:50%;background:var(--brown);display:block}
.links{list-style:none;font-size:14px;line-height:28px}
.links li{padding-left:16px;position:relative}
.links li:before{content:"";position:absolute;left:0;top:11px;width:6px;height:6px;border-radius:50%;background:var(--brown)}
.post{display:flex;gap:12px;margin-bottom:16px}
.post i{width:60px;height:56px;border-radius:4px;background:linear-gradient(135deg,#c8a27c,#7b5a44);display:block}
.post b{display:block;font-size:13px;margin-top:6px}
.post small{font-size:11px;color:var(--muted)}
.tags{display:flex;flex-wrap:wrap;gap:10px;width:300px}
.tags span{border:1px solid #999;font-size:12px;padding:4px 10px}
.copy{position:absolute;left:0;top:3480px;width:1200px;border-top:1px solid var(--line);text-align:center;font-size:13px;padding-top:20px;color:var(--muted)}
</style>
</head>
<body>

<header>
  <div class="topbar">
    <div class="contact-item" style="left:700px">
      <svg width="16" height="12" viewBox="0 0 16 12"><rect x="1" y="1" width="14" height="10" fill="none" stroke="#fff" stroke-width="1.5"/><path d="M1 1l7 6 7-6" fill="none" stroke="#fff" stroke-width="1.5"/></svg>
      <b>Email address</b>hello@tailbrook.com</div>
    <div class="contact-item" style="left:860px">
      <svg width="14" height="14" viewBox="0 0 14 14"><path d="M3 1l3 3-2 2c1 2 2 3 4 4l2-2 3 3-2 3C6 13 1 8 1 3z" fill="#fff"/></svg>
      <b>Phone</b>100-000-0000</div>
    <div class="contact-item" style="left:1000px">
      <svg width="14" height="14" viewBox="0 0 14 14"><circle cx="7" cy="7" r="6" fill="none" stroke="#fff" stroke-width="1.5"/><path d="M7 3v4h3" fill="none" stroke="#fff" stroke-width="1.5"/></svg>
      <b>Working hours</b>Mon-Fri 9:00am-7:00pm</div>
  </div>
  <div class="logo-tab"><span class="logo-dot"></span><span class="logo">Tailbrook</span></div>
  <nav class="nav">
    <ul><li>Home</li><li>About Us</li><li>Our Services</li><li>Our Blog</li><li>Contact Us</li></ul>
    <div class="social" style="left:950px"><span></span><span></span><span></span></div>
  </nav>
</header>

<section class="hero" role="img" aria-label="Close-up photo of a groomed small terrier">
  <h1>Tailbrook<br>Dog Grooming</h1>
  <p>Lorem ipsum dolor sit amet, consectetur adipiscing elit, sed do eiusmod tempor.</p>
  <a class="btn btn-lime abs" style="left:100px;top:370px">Book Online <i></i></a>
</section>

<section class="grooming">
  <h2 class="sec-title" style="top:775px">Dog Grooming</h2>
  <p class="sec-lead" style="top:826px">Lorem ipsum dolor sit amet, consectetur adipiscing elit, sed do eiusmod tempor incididunt ut labore et dolore magna aliqua.</p>

  <div class="card" style="left:130px">
    <div class="card-img" role="img" aria-label="Illustration of a dog in a grooming tub" style="background:linear-gradient(135deg,#f4c6dc,#e78fb8)"></div>
    <h3>How we Work</h3>
    <p>Lorem ipsum dolor sit amet, consectetur adipiscing elit, sed do eiusmod tempor incididunt.</p>
    <a class="btn btn-brown">Learn More <i></i></a>
  </div>
  <div class="card featured" style="left:450px">
    <div class="card-img" role="img" aria-label="Illustration of a dog wrapped in a towel" style="background:linear-gradient(135deg,#fff1b0,#f2c33a)"></div>
    <h3>How we Work</h3>
    <p>Lorem ipsum dolor sit amet, consectetur adipiscing elit, sed do eiusmod tempor incididunt.</p>
    <a class="btn btn-brown">Learn More <i></i></a>
  </div>
  <div class="card" style="left:770px">
    <div class="card-img" role="img" aria-label="Illustration of a dog with grooming tools" style="background:linear-gradient(135deg,#efd8e8,#b79a8c)"></div>
    <h3>How we Work</h3>
    <p>Lorem ipsum dolor sit amet, consectetur adipiscing elit, sed do eiusmod tempor incididunt.</p>
    <a class="btn btn-brown">Learn More <i></i></a>
  </div>
</section>

<section class="services">
  <h2 class="sec-title">Our Services</h2>
  <p class="sec-lead">Lorem ipsum dolor sit amet, consectetur adipiscing elit, sed do eiusmod tempor incididunt ut labore et dolore magna aliqua. Quis ipsum.</p>

  <div class="svc" style="left:120px;top:232px"><span class="num">1</span><h4>Styling</h4><p>Lorem ipsum dolor sit amet, consectetur adipiscing elit, sed do eiusmod tempor.</p><a class="btn btn-white">Explore Now <i></i></a></div>
  <div class="svc" style="left:120px;top:500px"><span class="num">3</span><h4>Full Grooming</h4><p>Lorem ipsum dolor sit amet, consectetur adipiscing elit, sed do eiusmod tempor.</p><a class="btn btn-white">Explore Now <i></i></a></div>
  <div class="svc" style="left:736px;top:232px"><span class="num">2</span><h4>Bath &amp; Tidy Up</h4><p>Lorem ipsum dolor sit amet, consectetur adipiscing elit, sed do eiusmod tempor.</p><a class="btn btn-white">Explore Now <i></i></a></div>
  <div class="svc" style="left:736px;top:500px"><span class="num">4</span><h4>Deluxe Bath</h4><p>Lorem ipsum dolor sit amet, consectetur adipiscing elit, sed do eiusmod tempor.</p><a class="btn btn-white">Explore Now <i></i></a></div>

  <div class="svc-photo" role="img" aria-label="Photo of a sitting golden puppy"></div>
</section>

<section class="work">
  <h2 class="sec-title" style="top:2232px">Our Work</h2>
  <p class="sec-lead" style="top:2284px">Lorem ipsum dolor sit amet, consectetur adipiscing elit, sed do eiusmod tempor incididunt ut labore et dolore magna aliqua. Quis ipsum.</p>
  <div class="work-img" role="img" aria-label="Photo of a freshly groomed terrier" style="left:100px;background:linear-gradient(160deg,#9ec3cf,#8a6a4c 60%,#5a3f2d)"></div>
  <div class="work-img" role="img" aria-label="Photo of a dog being groomed, darkened" style="left:440px;background:linear-gradient(160deg,#6a5444,#3e3028)"><span class="work-label">Full Grooming</span></div>
  <div class="work-img" role="img" aria-label="Photo of a paw getting its nails trimmed" style="left:780px;background:linear-gradient(160deg,#b8dceb,#d9b9a2 55%,#8c6d58)"></div>
</section>

<section class="newsletter">
  <h2>Subscribe to our Newsletter</h2>
  <p>Lorem ipsum dolor sit amet, consectetur adipiscing elit.</p>
  <div class="field">Enter Your Email</div>
  <div class="submit">Submit</div>
</section>

<footer>
  <div class="foot-col" style="left:100px">
    <div class="foot-logo"><span class="logo-dot"></span><span class="logo">Tailbrook</span></div>
    <div class="foot-info">
      <div><b>Address:</b> Lorem ipsum dolor</div>
      <div><b>Phone:</b> 100-000-0000</div>
      <div><b>Email:</b> info@tailbrook.com</div>
      <div><b>Website:</b> www.tailbrook.com</div>
    </div>
    <div class="foot-social"><span></span><span></span><span></span><span></span></div>
  </div>
  <div class="foot-col" style="left:400px">
    <h4>Quick Link</h4>
    <ul class="links"><li>Home</li><li>About Us</li><li>Our Services</li><li>Our Blog</li><li>Contact Us</li></ul>
  </div>
  <div class="foot-col" style="left:580px">
    <h4>Recent posts</h4>
    <div class="post"><i role="img" aria-label="Post thumbnail photo"></i><div><b>Lorem Ipsum</b><small>September 18 2021</small></div></div>
    <div class="post"><i role="img" aria-label="Post thumbnail photo"></i><div><b>Lorem Ipsum</b><small>September 18 2021</small></div></div>
    <div class="post"><i role="img" aria-label="Post thumbnail photo"></i><div><b>Lorem Ipsum</b><small>September 18 2021</small></div></div>
  </div>
  <div class="foot-col" style="left:810px">
    <h4>Product tags</h4>
    <div class="tags"><span>Lorem Ip</span><span>Lorem</span><span>Lorem</span><span>Lorem</span><span>Lorem</span><span>Lorem</span><span>Lorem Ipsu</span><span>Lorem</span><span>Lorem Ipsu</span><span>Lorem</span><span>Lorem</span><span>Lorem</span></div>
  </div>
  <div class="copy">©Copyrights 2025 Company Name &nbsp;|&nbsp; All Rights Reserved</div>
</footer>

</body>
</html>
```